KelvoSHIELD Brochure

We need a new brochure designed for our KelvoSHIELD Unit. I have provided examples of previous and words for the new ones. Stock photos will be purchased and forwarded once design is complete.

I have also attached a competitors product brochure for reference. This is a bout conveying by using our product your people will be safe and will not need to use high rated PPE
Updates

Project Deadline Extended
Reason: Will be extending the project for 1 day and selecting the final design tomorrow to allow some of you to fine tune submissions.

Target Market(s)

Professionals

Industry/Entity Type

Product

Contact Information for Business Card

Refer Attached Details

Requirements
Must have
• Brantley Osgood Logo and Colours Business Card
• Brochure should complement KelvoSHIELD Logo

```html
<!DOCTYPE html>
<html lang="en">
<head>
<meta charset="utf-8">
<title>Brantley Osgood – Business Card</title>
<link rel="stylesheet" href="https://fonts.googleapis.com/css2?family=Open+Sans:wght@400;600;700&display=swap">
<style>
  :root {
    --bg: #e9ebee;
    --blue-deep: #0b4f8a;
    --blue-mid: #1a74b8;
    --blue-bright: #2a8fd4;
    --white: #ffffff;
    --ink: #4a4d52;
    --ink-soft: #7a7e84;
    --rule: #c9ccd1;
  }
  * { box-sizing: border-box; margin: 0; padding: 0; }
  html, body { width: 1200px; height: 872px; overflow: hidden; }
  body {
    background: var(--bg);
    font-family: "Open Sans", Arial, sans-serif;
    position: relative;
  }
  .card {
    position: absolute;
    top: 291px;
    width: 500px;
    height: 290px;
    border-radius: 4px;
    overflow: hidden;
    box-shadow: 0 6px 18px rgba(0,0,0,.14);
  }
  /* Front */
  .card-front { left: 70px; background: var(--white); }
  .front-field {
    position: absolute; inset: 0 0 48px 0;
    background: radial-gradient(ellipse at 35% 30%, var(--blue-bright) 0%, var(--blue-mid) 45%, var(--blue-deep) 100%);
    color: var(--white);
    display: flex; flex-direction: column; align-items: center; justify-content: center;
    text-align: center;
  }
  .brand-lockup { display: flex; align-items: center; gap: 12px; margin-bottom: 14px; }
  .brand-square { width: 34px; height: 34px; background: var(--white); }
  .brand-name { font-size: 30px; font-weight: 700; letter-spacing: .5px; }
  .front-tagline { font-size: 17px; font-weight: 600; margin-bottom: 6px; }
  .front-roles { font-size: 11.5px; letter-spacing: .3px; opacity: .95; margin-bottom: 18px; }
  .front-web { font-size: 12px; font-weight: 600; }
  .front-strip { position: absolute; left: 0; right: 0; bottom: 0; height: 48px; background: var(--white); }

  /* Back */
  .card-back { left: 630px; background: var(--white); color: var(--ink); }
  .back-brand {
    position: absolute; left: 0; top: 0; bottom: 0; width: 118px;
    border-right: 1px solid var(--rule);
    display: flex; flex-direction: column; align-items: center; padding-top: 30px; gap: 10px;
  }
  .back-brand .brand-square { width: 40px; height: 40px; background: var(--blue-mid); }
  .back-brand .brand-name { font-size: 11px; font-weight: 700; color: var(--blue-mid); letter-spacing: 0; text-align: center; line-height: 1.3; }
  .contact-list {
    position: absolute; right: 22px; top: 26px; width: 340px;
    list-style: none; font-size: 9.5px; line-height: 1.45; color: var(--ink-soft); text-align: right;
  }
  .contact-list li { display: flex; justify-content: flex-end; align-items: flex-start; gap: 10px; margin-bottom: 9px; }
  .contact-icon { flex: none; width: 13px; height: 13px; margin-top: 1px; }
  .person { position: absolute; left: 140px; bottom: 26px; }
  .person-name { font-size: 24px; font-weight: 700; color: var(--ink); line-height: 1.1; }
  .person-name .first { color: var(--blue-mid); }
  .person-creds { font-size: 8px; color: var(--ink-soft); margin-top: 4px; line-height: 1.4; }
  .person-title { font-size: 14px; font-weight: 600; color: var(--ink); margin-top: 4px; }
</style>
</head>
<body>
  <section class="card card-front">
    <div class="front-field">
      <div class="brand-lockup">
        <span class="brand-square"></span>
        <span class="brand-name">Brantley Osgood</span>
      </div>
      <p class="front-tagline">Technology &amp; Innovation Professional</p>
      <p class="front-roles">Project Managers &nbsp;|&nbsp; Engineers &nbsp;|&nbsp; Operations Technologists</p>
      <p class="front-web">www.brantleyosgood.com.au</p>
    </div>
    <div class="front-strip"></div>
  </section>

  <section class="card card-back">
    <div class="back-brand">
      <span class="brand-square"></span>
      <span class="brand-name">Brantley Osgood</span>
    </div>
    <ul class="contact-list">
      <li>
        <span>Level 14 (Harbourline House)<br>88 Wattle Street, Brisbane Australia 4000<br>PO Box 455 Norvale QLD Australia 4012</span>
        <svg class="contact-icon" viewBox="0 0 14 14"><path d="M7 1a4 4 0 0 0-4 4c0 3 4 8 4 8s4-5 4-8a4 4 0 0 0-4-4z" fill="#1a74b8"/><circle cx="7" cy="5" r="1.5" fill="#fff"/></svg>
      </li>
      <li>
        <span>P +61 7 3100 2244 &nbsp; F +61 7 3100 2245 &nbsp; M +61 400 118 907</span>
        <svg class="contact-icon" viewBox="0 0 14 14"><path d="M3 1.5l2.5 0 1 3-1.5 1a7 7 0 0 0 3.5 3.5l1-1.5 3 1v2.5c0 .6-.5 1-1 1A10.5 10.5 0 0 1 2 2.5c0-.5.4-1 1-1z" fill="#1a74b8"/></svg>
      </li>
      <li>
        <span>dale.moreton@brantleyosgood.com.au</span>
        <svg class="contact-icon" viewBox="0 0 14 14"><circle cx="7" cy="7" r="6.5" fill="#1a74b8"/><text x="7" y="10" font-size="9" text-anchor="middle" fill="#fff" font-family="Arial, sans-serif">@</text></svg>
      </li>
      <li>
        <span>www.brantleyosgood.com.au</span>
        <svg class="contact-icon" viewBox="0 0 14 14"><circle cx="7" cy="7" r="6" fill="none" stroke="#1a74b8" stroke-width="1.4"/><ellipse cx="7" cy="7" rx="2.6" ry="6" fill="none" stroke="#1a74b8" stroke-width="1"/><line x1="1" y1="7" x2="13" y2="7" stroke="#1a74b8" stroke-width="1"/></svg>
      </li>
    </ul>
    <div class="person">
      <p class="person-name"><span class="first">Dale</span> Moreton</p>
      <p class="person-creds">CPEng, RPEQ, NER<br>BEng (Mech) MBA FIEAust</p>
      <p class="person-title">Executive Engineer</p>
    </div>
  </section>
</body>
</html>
```